Welbourne Dental, P.C. New stationary and business card for modern Dental Office

We need a new stationary/envelope/business card design using our newly designed logo. We are looking for an upscale look. Our new logo is used on our signage, using black as the background and white for the lettering. We would like the stationary to have black, white, possible greys or silver. We are looking for a letterhead, envelope, and business card design for three different employees, as well as a 4th card, same design, but just general with no employee name.

Project Deadline Extended
Reason: We began this project in the middle of our move into our new office. Things got pretty hectic and we just didn't have the time to go through designs. We now settled in and finally eliminated the designs that didn't work for us. We would like to extend the project another 5 days, and then finalize our decision. Most of the submissions showed business cards alone, with no stationary designs. Our original request was for stationary and business cards. Please keep this in mind.

Target Market(s)

Dental patients expecting high quality, cosmetic dentistry

Industry/Entity Type

Business

Contact Information for Business Card

Will need a design using our logo. All cards will be the same, other than that one card will have Office Managers name, One for the Doctor, Hygienist,
1. Office Manager - Marisol Dubrovka
2. Hygienist - Kayleigh Morrow
3. Gordon T. Welbourne, D.D.S.
4. One general one with no staff names

Font styles to use
Other font styles liked:
• see upload

Colors
000000
1b1b1b
757575
c9c9c9
e8e8e8
ffffff

Requirements
Must have
• -Logo
• -Phone number (718)555-0193
• -Address: 4352 63rd Ave
• Lower Level
• Brooklyn, NY 11290

```html
<!DOCTYPE html>
<html lang="en">
<head>
<meta charset="utf-8">
<title>Welbourne Dental, P.C. — Stationery Set</title>
<link rel="stylesheet" href="https://fonts.googleapis.com/css2?family=Lato:wght@400;700&display=swap">
<style>
  :root {
    --ink: #000000;
    --ink-soft: #1b1b1b;
    --grey: #757575;
    --silver: #c9c9c9;
    --mist: #e8e8e8;
    --paper: #ffffff;
    --edge: #8a8a8a;
  }
  html, body {
    margin: 0;
    padding: 0;
    width: 1200px;
    height: 1200px;
    overflow: hidden;
    background: var(--paper);
  }
  .stationery-set {
    display: block;
    width: 1200px;
    height: 1200px;
    font-family: "Lato", "Helvetica Neue", Arial, sans-serif;
  }
  .sheet-edge { fill: var(--paper); stroke: var(--edge); stroke-width: 1; }
  .band-ink { fill: var(--ink); }
  .swoosh-silver { fill: var(--silver); }
  .swoosh-white { fill: var(--paper); }
  .arc-silver { fill: none; stroke: var(--silver); stroke-width: 5; }
  .arc-ink { fill: none; stroke: var(--ink); stroke-width: 5; }
  .brand-name { fill: var(--paper); font-weight: 700; }
  .brand-name--dark { fill: var(--ink-soft); font-weight: 700; }
  .contact-line { fill: var(--ink-soft); font-weight: 400; }
  .contact-phone { fill: var(--ink); font-weight: 700; }
  .card-name { fill: var(--ink); font-weight: 700; }
  .card-role { fill: var(--grey); font-weight: 400; }
</style>
</head>
<body>
<svg class="stationery-set" viewBox="0 0 1200 1200" width="1200" height="1200" xmlns="http://www.w3.org/2000/svg">
  <defs>
    <clipPath id="letterhead-clip"><rect x="0" y="0" width="716" height="1012"/></clipPath>
    <clipPath id="flap-clip">
      <path d="M756 142 L768 62 Q774 30 806 30 L1130 30 Q1162 30 1168 62 L1174 142 Z"/>
    </clipPath>
    <clipPath id="envelope-clip"><rect x="756" y="142" width="418" height="928"/></clipPath>
    <clipPath id="card-clip"><rect x="338" y="1014" width="314" height="184"/></clipPath>
  </defs>

  <!-- Letterhead -->
  <g class="letterhead">
    <rect class="sheet-edge" x="0.5" y="0.5" width="715" height="1011"/>
    <g class="letterhead-header" clip-path="url(#letterhead-clip)">
      <circle class="swoosh-silver" cx="192" cy="-42" r="200"/>
      <circle class="swoosh-white" cx="182" cy="-46" r="193"/>
      <circle class="band-ink" cx="178" cy="-34" r="182"/>
      <circle class="swoosh-white" cx="170" cy="-34" r="175"/>
      <circle class="band-ink" cx="162" cy="-30" r="164"/>
      <text class="brand-name" x="72" y="72" font-size="15">Welbourne Dental, P.C.</text>
    </g>
    <g class="letterhead-footer">
      <path class="band-ink" d="M0 950 L62 950 L68 958 L0 958 Z"/>
      <path class="band-ink" d="M476 950 L716 950 L716 958 L470 958 Z"/>
      <text class="contact-line" x="71" y="959" font-size="12.5" textLength="397" lengthAdjust="spacingAndGlyphs">4352 63rd Ave, Lower Level, Brooklyn, NY  11290   |   Ph: (718)555-0193</text>
    </g>
  </g>

  <!-- Envelope -->
  <g class="envelope">
    <rect class="sheet-edge" x="756.5" y="142" width="417" height="928"/>
    <path class="band-ink" d="M756 142 L768 62 Q774 30 806 30 L1130 30 Q1162 30 1168 62 L1174 142 Z"/>
    <g clip-path="url(#flap-clip)">
      <circle class="arc-silver" cx="978" cy="2" r="132"/>
      <circle class="arc-silver" cx="975" cy="-6" r="125"/>
    </g>
    <g class="envelope-mark" clip-path="url(#envelope-clip)">
      <circle class="arc-ink" cx="1140" cy="930" r="128"/>
      <circle class="arc-silver" cx="1150" cy="940" r="122"/>
      <circle class="swoosh-white" cx="1148" cy="932" r="118"/>
    </g>
    <text class="brand-name--dark" font-size="15" transform="translate(1100 1040) rotate(-90)">Welbourne Dental, P.C.</text>
    <text class="contact-line" font-size="12.5" transform="translate(1135 682) rotate(-90)" textLength="426" lengthAdjust="spacingAndGlyphs">4352 63rd Ave, Lower Level, Brooklyn, NY  11290   |   Ph: (718)555-0193</text>
  </g>

  <!-- Business card -->
  <g class="business-card">
    <rect class="sheet-edge" x="338.5" y="1014.5" width="313" height="183"/>
    <g clip-path="url(#card-clip)">
      <circle class="swoosh-silver" cx="428" cy="996" r="110"/>
      <circle class="swoosh-white" cx="421" cy="993" r="105"/>
      <circle class="band-ink" cx="424" cy="1000" r="101"/>
      <circle class="swoosh-white" cx="418" cy="1000" r="97"/>
      <circle class="band-ink" cx="414" cy="1002" r="92"/>
      <text class="brand-name" x="372" y="1054" font-size="10.5">Welbourne Dental, P.C.</text>
    </g>
    <text class="card-name" x="558" y="1037" font-size="8.5">Name</text>
    <text class="card-role" x="558" y="1048" font-size="7.5">Designation</text>
    <text class="contact-line" x="602" y="1169" font-size="7.5" text-anchor="end">4352 63rd Ave, Lower Level, Brooklyn, NY 11290</text>
    <text class="contact-phone" x="602" y="1180" font-size="7.5" text-anchor="end">Ph: (718)555-0193</text>
    <rect class="band-ink" x="608" y="1163" width="2" height="19"/>
    <rect class="band-ink" x="616" y="1163" width="36" height="19"/>
  </g>
</svg>
</body>
</html>
```